Mobile Home Page Design for “Zarvo for Plumbers” – in Figma

PipeDashly: Fast, Reliable Emergency Plumbing at Your Fingertips

PipeDashly is a streamlined platform connecting homeowners with trusted, local plumbers for urgent repairs—whether it’s a burst pipe, leak, or blocked toilet. Designed for speed and peace of mind, our homepage will be clean, modern, and mobile-optimized to guide users from problem to solution in minutes.

Our primary users are homeowners in stressful situations who care most about price transparency and how fast help can arrive. Bookings are made exclusively online, so the user experience must instill confidence and eliminate hesitation.

The call-to-action should be immediate and persuasive—"See Prices & Book" will be prominently featured as the main CTA. Additional trust-builders could include:

A simple 3-step booking illustration (Tell us what’s wrong → See prices → Get a plumber)
Customer reviews or “Trusted by 10,000+ homeowners” badges

Display real-time availability ("Next plumber available in 40 minutes")
Price estimates upfront—with clear service types

Target Market(s)

Home Owners: 35-65 Years old.

Industry/Entity Type

Home Services.

Number of Pages Required

1 page

Font styles to use
Sans Serif

Colors
0054AA
0677BA
7BADD7
CADEEF
E8F1F8
FFF300
FFF600
FEFA6F
FFFEC7
FFFEE8

Requirements
Nice to have
• Map showing that plumbers are nearby. Trustworthy look and feel. Blue/Red or Blue/Yellow.

```html
<!DOCTYPE html>
<html lang="en">
<head>
<meta charset="utf-8">
<title>PipeDashly – Mobile Home Page Screens</title>
<link href="https://fonts.googleapis.com/css2?family=Poppins:wght@400;500;600&display=swap" rel="stylesheet">
<style>
:root{
  --blue-deep:#0054AA;
  --blue-mid:#0677BA;
  --blue-soft:#7BADD7;
  --blue-pale:#CADEEF;
  --blue-mist:#E8F1F8;
  --yellow:#FFF300;
  --grey-badge:#c9d2dc;
  --ink:#1b1b22;
  --white:#ffffff;
  --bg:#ffffff;
}
*{box-sizing:border-box;margin:0;padding:0}
html,body{width:1200px;height:980px;overflow:hidden;background:var(--bg)}
body{font-family:'Poppins',sans-serif;color:var(--ink);position:relative}
.screen{position:absolute;width:162px;height:336px;border-radius:20px;overflow:hidden;background:var(--blue-mist);box-shadow:0 0 0 1px #e3e8ef}
.r1{top:126px}.r2{top:512px}
.c1{left:187px}.c2{left:401px}.c3{left:625px}.c4{left:851px}
.center{text-align:center}
.h{font-weight:500;font-size:11px;line-height:1.45}
.s{font-size:6.4px;line-height:1.55}
.xs{font-size:4.6px;line-height:1.6}
.btn{display:block;background:var(--yellow);border-radius:4px;text-align:center;font-size:6.6px;font-weight:500;padding:6px 0}
.photo{background:linear-gradient(160deg,var(--blue-pale),var(--blue-soft) 70%,var(--blue-mid))}
.wordmark{font-size:7px;font-weight:500}
.pill{display:flex;align-items:center;justify-content:center;gap:5px;border:1px solid #e0e6ee;border-radius:14px;background:#fff;font-size:5.4px;font-weight:500;height:24px}
.top-bar{display:flex;justify-content:space-between;align-items:center;padding:10px 10px 0}
.grad-top{background:linear-gradient(180deg,var(--blue-pale),var(--blue-mist) 45%)}
.tiles{display:flex;gap:7px;padding:0 7px}
.tile{flex:1;text-align:center}
.tile .box{height:44px;border-radius:3px;background:#fff;display:flex;align-items:center;justify-content:center}
.tile.on .box{background:var(--yellow)}
.tile span{display:block;font-size:5.2px;margin-top:6px}
.areas{margin:10px 7px 0;border:1px solid var(--blue-mid);border-radius:18px;padding:14px 16px 0;background:var(--blue-mist)}
.area{border-bottom:1px solid #d3dbe5;padding-bottom:12px;margin-bottom:14px;text-align:center}
.area b{font-weight:500;font-size:7px;display:block;margin-bottom:6px}
.map{margin:0 7px;height:110px;border:1px solid var(--blue-mid);border-radius:16px;background:linear-gradient(135deg,#f0f1f3,#dfe2e6)}
.partners{display:flex;align-items:center;justify-content:center;gap:10px;margin-top:36px}
.partner-badge{width:30px;height:22px;border-radius:4px;background:var(--grey-badge)}
.table{font-size:5.4px}
.table div{display:grid;grid-template-columns:74px 1fr;padding:0 10px;height:16.3px;align-items:center}
.table div:nth-child(even){background:#fff}
.faq{margin:0 7px 6px;background:#fff;border-radius:4px;padding:7px 10px 7px 13px;display:flex;justify-content:space-between;align-items:center;font-size:5px;line-height:1.5}
.faq.open{background:var(--yellow);display:block;margin-left:20px;margin-right:7px;padding:8px 12px}
.footer{background:var(--blue-deep);color:#fff}
</style>
</head>
<body>

<section class="screen r1 c1">
  <div class="top-bar">
    <div class="wordmark">PipeDashly</div>
    <svg width="9" height="8" viewBox="0 0 9 8"><path d="M0 1h9M0 4h9M0 7h9" stroke="#1b1b22" stroke-width=".8"/></svg>
  </div>
  <p class="center s" style="color:var(--blue-deep);margin-top:16px">*12 Plumbers on-call near you</p>
  <h1 class="center h" style="margin-top:4px">Book a Plumber near<br>you - fast</h1>
  <a class="btn" style="margin:8px 20px 0">Book Now</a>
  <p class="center s" style="margin-top:10px">Get an instant response from a<br>trusted plumber 24/7</p>
  <div class="photo" role="img" aria-label="Smiling plumber in cap and overalls holding a wrench and hose" style="position:absolute;left:14px;right:14px;bottom:0;height:185px;border-radius:60px 60px 0 0"></div>
</section>

<section class="screen r1 c2 grad-top">
  <h2 class="center h" style="margin-top:26px;margin-bottom:6px">All our Plumbers are</h2>
  <div class="tiles">
    <div class="tile on"><div class="box"><svg width="20" height="16" viewBox="0 0 20 16"><path d="M3 12a7 7 0 0 1 14 0z" fill="var(--blue-deep)"/><rect x="1" y="12" width="18" height="3" rx="1" fill="var(--blue-deep)"/><path d="M8 5v7M12 5v7" stroke="var(--yellow)"/></svg></div><span>Experienced</span></div>
    <div class="tile"><div class="box"><svg width="18" height="18" viewBox="0 0 18 18"><path d="M3 17V9a5 5 0 0 1 5-5h6" fill="none" stroke="var(--blue-deep)" stroke-width="3.5"/><rect x="13" y="1" width="3" height="7" fill="var(--blue-deep)"/></svg></div><span>Verified</span></div>
    <div class="tile"><div class="box"><svg width="16" height="18" viewBox="0 0 16 18"><path d="M8 1 15 3v6c0 4-3 7-7 8-4-1-7-4-7-8V3z" fill="var(--blue-deep)"/><path d="m5 9 2 2 4-4" fill="none" stroke="#fff" stroke-width="1.4"/></svg></div><span>Insured</span></div>
  </div>
  <h2 class="center h" style="margin-top:22px">Service Areas</h2>
  <div class="areas">
    <div class="area"><b>Plumbing</b><p class="xs" style="font-size:5px">We offer all solutions to all your plumbing problems from leaks to blocked toilets</p></div>
    <div class="area"><b>Heating</b><p class="xs" style="font-size:5px">We offer all solutions to all your plumbing problems from leaks to blocked toilets</p></div>
    <div class="area" style="border:0"><b>Drainage</b></div>
  </div>
</section>

<section class="screen r1 c3">
  <div style="margin:-14px 18px 0;background:#fff;border-radius:0 0 14px 14px;height:34px;padding-top:16px" class="center xs">Get an instant response &amp; book</div>
  <p class="center xs" style="font-size:5.2px;margin-top:13px">Track your plumber en route to you</p>
  <h2 class="center h" style="margin-top:38px">Call an<br>PipeDashly now</h2>
  <p class="center s" style="margin-top:4px">We have plumbers near you<br>ready to assist 24/7</p>
  <div class="map" role="img" aria-label="Street map of the area showing nearby plumbers" style="margin-top:14px"></div>
  <a class="btn" style="margin:16px 20px 0">Call a Plumber Now</a>
</section>

<section class="screen r1 c4" style="background:#fff">
  <div class="photo" role="img" aria-label="Smiling plumber in cap and blue overalls writing on a clipboard" style="height:206px"></div>
  <div style="position:absolute;top:206px;left:0;right:0;bottom:0;background:var(--blue-pale);border-radius:18px 18px 0 0">
    <h2 class="center h" style="margin-top:26px">Why customers love<br>PipeDashly?</h2>
    <div style="position:absolute;left:7px;right:7px;top:76px;bottom:0;background:var(--blue-mist);border-radius:18px 18px 0 0;padding:14px 12px">
      <div class="pill"><svg width="9" height="9" viewBox="0 0 10 10"><path d="M9 5a4 4 0 1 1-1.2-2.8M5 3v2l1.5 1" fill="none" stroke="#1b1b22" stroke-width=".8"/></svg>Available 24/7</div>
    </div>
  </div>
</section>

<section class="screen r2 c1 grad-top">
  <h2 class="center h" style="margin-top:26px">Why customers love<br>PipeDashly?</h2>
  <div style="margin:14px 6px 0;background:var(--white);border-radius:18px;padding:14px 12px;display:grid;gap:5px">
    <div class="pill"><svg width="9" height="9" viewBox="0 0 10 10"><path d="M9 5a4 4 0 1 1-1.2-2.8M5 3v2l1.5 1" fill="none" stroke="#1b1b22" stroke-width=".8"/></svg>Available 24/7</div>
    <div class="pill"><svg width="9" height="9" viewBox="0 0 10 10"><path d="M1 5 5 1h4v4L5 9z" fill="none" stroke="#1b1b22" stroke-width=".8"/><circle cx="7" cy="3" r=".7"/></svg>Up-front Pricing</div>
    <div class="pill"><svg width="9" height="9" viewBox="0 0 10 10"><path d="M1 4a4 4 0 0 1 7-2M9 6a4 4 0 0 1-7 2" fill="none" stroke="#1b1b22" stroke-width=".8"/></svg>Immediate response</div>
  </div>
  <div class="partners" aria-label="Accreditation partners">
    <span class="partner-badge"></span>
    <span class="partner-badge"></span>
    <span class="partner-badge"></span>
    <span class="partner-badge"></span>
  </div>
  <h2 class="center h" style="margin-top:30px">We’re expanding into<br>all the major boroughs<br>in London &amp; Essex</h2>
</section>

<section class="screen r2 c2">
  <div class="table" style="margin-top:-8px">
    <div><span>Ealing</span><span>Newham</span></div>
    <div><span>Enfield</span><span>Redbridge</span></div>
    <div><span>Greenwich</span><span>Richmond upon Thames</span></div>
    <div><span>Hackney</span><span>Southwark</span></div>
    <div><span>Hammersmith &amp; Fulham</span><span>Sutton</span></div>
    <div><span>Haringey</span><span>Tower Hamlets</span></div>
    <div><span>Harrow</span><span>Waltham Forest</span></div>
    <div><span>Havering</span><span>Wandsworth</span></div>
    <div><span>Hillingdon</span><span>Westminster</span></div>
  </div>
  <h2 class="center h" style="margin-top:42px">Customer Feedback</h2>
  <p class="center s">We serve customers instantly across<br>the whole of London</p>
  <svg style="display:block;margin:10px auto 0" width="56" height="9" viewBox="0 0 56 9"><g fill="none" stroke="var(--blue-deep)" stroke-width=".6"><path id="st" d="M4.5 .5l1.2 2.6 2.8.3-2.1 1.9.6 2.8-2.5-1.4-2.5 1.4.6-2.8L.5 3.4l2.8-.3z"/><use href="#st" x="12"/><use href="#st" x="24"/><use href="#st" x="36"/><use href="#st" x="48"/></g></svg>
  <svg style="display:block;margin:8px auto 0" width="28" height="18" viewBox="0 0 28 18"><path d="M2 18V11C2 5 6 1 12 0v4C9 5 8 7 8 10h4v8zM16 18V11c0-6 4-10 10-11v4c-3 1-4 3-4 6h4v8z" fill="var(--blue-deep)"/></svg>
  <p class="center xs" style="font-size:5.2px;margin-top:6px">Was here in under 15 minutes to<br>fix my leak at midnight!</p>
  <div style="display:flex;gap:4px;justify-content:center;margin-top:14px"><i style="width:5px;height:5px;border-radius:50%;background:var(--blue-deep)"></i><i style="width:5px;height:5px;border-radius:50%;background:var(--yellow);border:1px solid #d9cf00"></i><i style="width:5px;height:5px;border-radius:50%;background:var(--yellow);border:1px solid #d9cf00"></i></div>
</section>

<section class="screen r2 c3">
  <h2 class="center h" style="margin:22px 0 14px">Frequently Asked<br>Questions</h2>
  <div class="faq"><span>How can you verify that<br>PipeDashly are reliable?</span><svg width="7" height="4" viewBox="0 0 7 4"><path d="m.5.5 3 3 3-3" fill="none" stroke="#1b1b22" stroke-width=".6"/></svg></div>
  <div class="faq open"><div style="display:flex;justify-content:space-between"><span>Are your plumbers registered with<br>HeatSafe Register?</span><svg width="7" height="4" viewBox="0 0 7 4"><path d="m.5 3.5 3-3 3 3" fill="none" stroke="#1b1b22" stroke-width=".6"/></svg></div>
    <p style="font-size:4.2px;line-height:1.6;margin-top:5px">Lorem ipsum is simply dummy text of the printing and typesetting industry. Lorem ipsum has been the industry’s standard dummy text ever since the 1500s, when an unknown printer took a galley of type and scrambled it to make a type specimen bo</p></div>
  <div class="faq"><span>Do your plumbers have<br>insurance?</span><svg width="7" height="4" viewBox="0 0 7 4"><path d="m.5.5 3 3 3-3" fill="none" stroke="#1b1b22" stroke-width=".6"/></svg></div>
  <div class="faq"><span>How much do your plumbers<br>cost?</span><svg width="7" height="4" viewBox="0 0 7 4"><path d="m.5.5 3 3 3-3" fill="none" stroke="#1b1b22" stroke-width=".6"/></svg></div>
  <div class="faq" style="height:24px"><span>Do you charge a call-out fee?</span><svg width="7" height="4" viewBox="0 0 7 4"><path d="m.5.5 3 3 3-3" fill="none" stroke="#1b1b22" stroke-width=".6"/></svg></div>
  <div style="position:absolute;left:0;right:0;bottom:0;height:32px;background:var(--blue-deep)"></div>
</section>

<section class="screen r2 c4 footer center">
  <div class="wordmark" style="margin-top:14px">PipeDashly</div>
  <p class="xs" style="font-size:5px;margin-top:12px">Created with in London<br>Registered in England and Wales<br>Company Number 999888877<br>ICO Registration AB9876543</p>
  <div style="width:40px;height:40px;border-radius:50%;background:var(--yellow);margin:14px auto 0"></div>
  <p style="font-size:6.6px;margin-top:16px">Address</p>
  <p class="xs" style="font-size:5px;margin-top:4px">18 Wharfside Lane<br>London, SE4 2RT. UK.</p>
  <div style="display:flex;gap:7px;justify-content:center;margin-top:18px"><i style="width:9px;height:9px;border-radius:50%;background:#fff"></i><i style="width:9px;height:9px;border-radius:50%;background:#fff"></i><i style="width:9px;height:9px;border-radius:50%;background:#fff"></i><i style="width:9px;height:9px;border-radius:50%;background:#fff"></i></div>
  <div style="display:flex;gap:12px;justify-content:center;margin-top:18px;font-size:6.2px">
    <span style="display:flex;align-items:center;gap:3px"><i style="width:8px;height:8px;border:1px solid #fff"></i>Phone Store</span>
    <span style="display:flex;align-items:center;gap:3px"><i style="width:8px;height:8px;border:1px solid #fff"></i>Droid Market</span>
  </div>
  <p style="font-size:4.2px;line-height:1.6;margin:20px 18px 0">pipedashly.example is a trading name of MyCompany Name Ltd, registered at Companies House in England and Wales under company registration number 3987889.</p>
  <p class="xs" style="font-size:5px;margin-top:14px">Privacy and Cookie Policy<br>Terms &amp; Conditions<br>Service Terms &amp; Conditions</p>
</section>

</body>
</html>
```